Lotvantage.com Webpage Design

Design Brief for lotvantage.com (Copy of Brief also in attached Word file)

Name of Website- lotvantage.com (existing logo and look & feel of website to be changed)

Logo - Finalised. The logo files are attached with the brief as “logo.jpeg”. The “Blue- Grey” version of the logo is for use on lighter backgrounds and the “Orange-White” version of the logo is for use on darker backgrounds. (A full Black version of the logo is also attached). Both versions may be used in different parts of the website. All attached files are in .png format.
Status - The website in functional and is undergoing user trials. However, we want to improve the look & feel of the website so at it seems
a. cotemporary,
b. Easy to Navigate
c. professional and
d. Vibrant.

Please visit ‘lotvantage.com’ to check out the website and its functionalities – please use it only as a reference for the features & functions to be provided, however the designer should use a ‘Free Hand’ in designing the composition of various parts of the webpage without getting too influenced by the existing design

Objective of the Website ‘lotvantage.com –
a. It is a portal focussed on listing of ‘Retail’ specific real-estate properties by developers, owners and realty brokers. The properties shall listed under the following four categories-
i. Retail Malls
ii. Shopping Complexes
iii. High-street shops
iv. Retail Warehouses
*refer lotvantage.com for better clarity

b. The abovementioned properties shall be listed either for ‘Sale’ or ‘rent\lease’ or both

c. Users shall visit the site in case they wish to acquire a retail \ shop space either on ‘sale’ or ‘rent’. These Users would be able to specify the ‘Search Criteria’ through the tool-bars provided on the website – the ‘Search Criteria’ shall comprise of ‘Type of space category’, ‘City’, ‘Locality’, transaction type ie ‘Rent \ Sale’ and ‘Area Range’

d. The main revenue model for the website shall be listing fee ( or advertising charges ) payable by those listing their properties on the website.

Three Main Pages of Website (lotvantage.com) that need to be designed -
a. Main Home Page (visit the web link - http://lotvantage.com/ ) - The main home page has the “Search Toolbar” for specifying of Search Criteria by the User. It shall also have the following features & functions-
i. Main Advertising Banner
ii. Featured Projects
iii. New Launches
iv. Toolbar with buttons – ‘Advertise with Us’, ‘Listings Alert’, ‘Lot Mavens’, ‘Advertiser Login’

b. Property Listings Page (visit the web link - http://lotvantage.com/gurgaon-in-india ) - The List of property options that match the Criteria specified by the ‘User’ get displayed on this page.

c. Property Detail Page - When the ‘User’ clicks on the “More….” Button on the ‘Property Listings Page’ (given in point b. above) the web page with the details of the property opens. (For Example – visit the web link - http://lotvantage.com/brevo-Shopping-Complex-brevo-quadrel-gurgaon-636 )

Note:- Please refer to attached ‘Shopping’ related images the designer may use them on the website to provide a look & feel of retail if required – either separately or rotate in a single window

Target Market(s)

Retailers & Investors looking for retail space, Real Estate Brokers, Developers

Industry/Entity Type

Advertising

Number of Pages Required

3 page

Requirements
Must have
• Refer to existing site lotvantage.com -- all the existing functionalities are a must have.
Nice to have
• The Designer may use the retail related images on the website if required for making it more vibrant. Refer attached images Shopping(1-6).jpg

```html
<!DOCTYPE html>
<html lang="en">
<head>
<meta charset="utf-8">
<title>Lotvantage.com – Home</title>
<link href="https://fonts.googleapis.com/css2?family=Roboto:wght@300;400;500;700&family=Roboto+Condensed:wght@400;700&display=swap" rel="stylesheet">
<style>
:root{
  --blue:#2aa6ea;
  --blue-dark:#1d8fd0;
  --ink:#333;
  --muted:#777;
  --line:#ddd;
  --grey-bg:#ebebeb;
  --dark:#2e2e2e;
  --darker:#1c1c1c;
  --card-bar:#3a3a3a;
  --white:#fff;
}
*{box-sizing:border-box;margin:0;padding:0}
html,body{width:1200px;height:3609px;overflow:hidden}
body{font-family:'Roboto',Arial,sans-serif;color:var(--ink);background:var(--white);position:relative}
.page{position:relative;width:1200px;height:3609px}
a{color:inherit;text-decoration:none}

/* header */
.site-header{position:absolute;top:0;left:0;width:1200px;height:100px;background:linear-gradient(#fafafa,#e6e6e6);border-bottom:1px solid #ccc}
.brand{position:absolute;left:18px;top:30px;display:flex;align-items:center;gap:10px}
.brand-dot{width:30px;height:30px;border-radius:50%;background:var(--blue)}
.brand-name{font-size:30px;font-weight:700;color:#2b6e9a;letter-spacing:-.5px}
.main-nav{position:absolute;left:420px;top:0;display:flex;height:100px}
.nav-home{width:75px;height:100px;background:var(--blue);display:flex;align-items:center;justify-content:center}
.nav-item{width:150px;height:100px;border-left:1px solid #d4d4d4;display:flex;flex-direction:column;justify-content:center;align-items:center;font-size:15px;color:#666;line-height:1.15;text-align:center}
.nav-item:last-child{width:120px;border-right:1px solid #d4d4d4}
.nav-item b{font-weight:500;color:#777;letter-spacing:.5px}
.account{position:absolute;right:50px;top:16px;text-align:center}
.account .register{font-size:12px;color:var(--blue);text-decoration:underline;display:block;margin-bottom:6px}
.account .login{display:block;width:170px;height:38px;line-height:38px;background:var(--blue);color:#fff;font-size:14px;border-radius:2px}

/* hero */
.hero{position:absolute;top:100px;left:0;width:1200px;height:500px;background:radial-gradient(ellipse at 55% 10%,#eef3f6 0%,#b7bdc2 30%,#6d6e70 60%,#3e3a38 100%)}
.hero-title{position:absolute;left:44px;top:222px;font-size:44px;font-weight:300;color:#fff;letter-spacing:.5px}
.hero-sub{position:absolute;left:44px;top:296px;font-size:22px;font-weight:300;color:#fff;line-height:1.3}

/* search */
.search-band{position:absolute;top:600px;left:0;width:1200px;height:240px;background:linear-gradient(#f4f4f4,#e9e9e9)}
.search-panel{position:absolute;top:590px;left:105px;width:990px;height:200px;background:#fff;box-shadow:0 8px 14px rgba(0,0,0,.18);padding:14px 40px}
.search-title{font-size:30px;font-weight:700;color:var(--blue);line-height:1}
.search-title span{font-size:22px;font-weight:400;color:#333}
.search-grid{display:grid;grid-template-columns:repeat(3,270px);column-gap:50px;row-gap:10px;margin-top:14px}
.field label{display:block;font-size:12px;color:#444;margin-bottom:4px;text-transform:uppercase;white-space:nowrap}
.select{height:26px;background:#f1f1f1;border:1px solid #d8d8d8;font-size:12px;color:#666;padding:0 8px;line-height:24px;position:relative}
.select::after{content:"";position:absolute;right:-1px;top:-1px;width:22px;height:26px;background:var(--blue)}
.select.text::after{display:none}
.search-btn{height:26px;width:150px;background:var(--blue);color:#fff;font-size:13px;text-align:center;line-height:26px;margin-top:19px}

/* welcome */
.welcome{position:absolute;top:840px;left:0;width:1200px;height:440px;background:linear-gradient(#e9e9e9,#f2f2f2)}
.welcome-text{position:absolute;left:88px;top:30px;width:500px}
.welcome-text h2{font-size:38px;font-weight:400;color:#555}
.welcome-text h2 span{font-size:28px;font-weight:700;color:var(--blue)}
.welcome-text p{font-size:15px;color:#666;line-height:1.5;margin-top:20px}
.audience{display:flex;margin-top:26px;gap:24px}
.audience h3{font-size:15px;font-weight:700;color:var(--blue)}
.audience ul{list-style:none;margin-top:4px}
.audience li{font-size:15px;color:#666;padding-left:18px;line-height:1.75;position:relative}
.audience li::before{content:"";position:absolute;left:0;top:10px;width:9px;height:1px;background:#666}
.audience-note{width:270px;font-size:15px;color:#666;line-height:1.45;border-left:3px solid #ccc;padding-left:10px;margin-left:20px}
.read-more{position:absolute;left:292px;top:382px;display:flex}
.read-more span{display:block;height:42px;line-height:42px;background:var(--blue);color:#fff;padding:0 34px;font-size:14px}
.read-more i{display:block;width:40px;height:42px;background:#222}
.category-card{position:absolute;left:615px;top:10px;width:520px;height:410px;background:#fff;box-shadow:0 6px 14px rgba(0,0,0,.2);padding:22px 30px}
.category-card p{font-size:12px;color:#999;line-height:1.5;text-align:center}
.carousel-arrows{display:flex;justify-content:flex-end;gap:4px;margin-top:14px}
.carousel-arrows span{width:22px;height:22px;background:#ddd}
.category-tiles{display:flex;gap:20px;margin-top:10px}
.tile{width:220px;height:200px;position:relative}
.tile .photo{width:100%;height:100%}
.tile-label{position:absolute;left:0;right:0;bottom:0;background:var(--blue);color:#fff;font-size:15px;font-weight:700;text-align:center;padding:12px 0}
.tile-label small{display:block;font-size:10px;font-weight:400;margin-top:2px}

/* featured */
.section-title{font-size:38px;font-weight:500;text-align:center;color:#333;letter-spacing:.5px}
.featured{position:absolute;top:1280px;left:0;width:1200px;height:1220px}
.featured .section-title{margin-top:85px}
.title-rule{width:1050px;margin:24px auto 0;border-top:1px solid var(--line)}
.filter-tabs{position:absolute;top:172px;left:195px;display:flex;align-items:center}
.filter-tabs span{font-size:14px;font-weight:500;color:#444;padding:0 38px;border-right:1px solid #ccc;line-height:14px}
.filter-tabs span:last-child{border-right:none}
.filter-tabs .active{background:var(--blue);color:#fff;padding:9px 38px;border:none;margin-right:8px}
.card-grid{position:absolute;left:75px;display:grid;grid-template-columns:repeat(4,252px);column-gap:14px}
.row-1{top:290px}.row-2{top:730px}
.card{height:410px;background:#fff;border:1px solid #e2e2e2;position:relative;display:flex;flex-direction:column}
.card .photo{height:165px;position:relative}
.tag{position:absolute;right:14px;top:0;width:60px;height:66px;background:#2f2f2f;color:#fff;font-size:13px;font-weight:700;text-align:center;padding-top:10px;line-height:1.2;clip-path:polygon(0 0,100% 0,100% 100%,50% 86%,0 100%)}
.card-type{height:28px;line-height:28px;text-align:center;font-size:13px;font-weight:500;color:#333;background:#f3f3f3;border-bottom:1px solid #e3e3e3}
.card-body{padding:12px 10px;flex:1}
.card-body h4{font-family:'Roboto Condensed',Arial,sans-serif;font-size:19px;font-weight:700;color:#333;margin-bottom:6px}
.card-body p{font-size:12.5px;color:#666;line-height:1.4}
.card.highlight .card-body{background:var(--blue)}
.card.highlight .card-body p{color:#fff}
.card.highlight .card-type{background:#fff}
.card-meta{background:var(--card-bar);color:#fff;font-size:11px}
.card-meta div{height:32px;display:flex;align-items:center;gap:8px;padding:0 10px;border-top:1px solid #4a4a4a}
.card-meta svg{flex:none}
.pagination{position:absolute;top:1170px;right:75px;display:flex;align-items:center;gap:4px;font-size:15px;color:#555}
.pagination span.box{width:26px;height:22px;border:1px solid #ccc;font-size:10px;color:#888;text-align:center;line-height:20px}
.pagination .label{margin-right:10px}

/* new launch */
.launch{position:absolute;top:2500px;left:0;width:1200px;height:480px;background:linear-gradient(90deg,#2b2a28,#6d6660 45%,#8a8681 60%,#3b3835)}
.launch .section-title{color:#fff;padding-top:32px}
.launch-card{position:absolute;left:240px;top:105px;width:645px;height:280px}
.launch-card .photo{position:absolute;inset:0}
.launch-tag{position:absolute;background:#1f1f1f;color:#fff;font-size:13px;font-weight:700;padding:6px 26px;transform:rotate(-45deg);transform-origin:left top;top:80px;left:4px}
.launch-bar{position:absolute;left:0;right:0;bottom:0;height:62px;background:#111;display:flex;align-items:center;color:#fff;font-size:17px;font-weight:700}
.launch-bar span{flex:1;text-align:center}
.launch-bar i{width:1px;height:30px;background:#888}
.launch-meta{position:absolute;top:400px;left:240px;width:645px;display:flex;align-items:center;justify-content:center;color:#fff;font-size:17px;font-weight:700;gap:30px}
.launch-meta i{width:1px;height:22px;background:#aaa}
.arrow{position:absolute;top:200px;width:30px;height:50px}
.arrow.left{left:50px}.arrow.right{right:50px}

/* contact */
.get-in-touch{position:absolute;top:2980px;left:0;width:1200px;height:375px;background:var(--dark);text-align:center;color:#bbb}
.get-in-touch h3{font-size:20px;font-weight:400;color:#fff;margin-top:100px}
.socials{display:flex;justify-content:center;gap:8px;margin-top:20px}
.socials span{width:36px;height:36px;border:1px solid #999;background:#3c3c3c}
.socials span:first-child{background:#fff}
.get-in-touch p{font-size:12px;color:#999;margin-top:16px}
.newsletter-input{width:420px;height:30px;margin:12px auto 0;background:#4a4a4a;text-align:left;padding-left:10px;line-height:30px;font-size:11px;color:#888}
.subscribe{width:120px;height:30px;margin:28px auto 0;border:1px solid #666;background:#222;color:#ddd;font-size:12px;line-height:28px}

/* footer */
.site-footer{position:absolute;top:3355px;left:0;width:1200px;height:254px;background:var(--darker);color:#ccc}
.footer-col h5{font-size:15px;font-weight:700;color:#fff;letter-spacing:.5px;margin-bottom:10px}
.footer-nav{position:absolute;left:66px;top:42px;display:flex;gap:70px}
.footer-nav ul{list-style:none}
.footer-nav li{font-size:14px;line-height:27px;padding-left:20px;position:relative}
.footer-nav li::before{content:"";position:absolute;left:0;top:8px;width:10px;height:10px;border-radius:50%;border:1px solid #aaa}
.footer-nav .two{margin-top:27px}
.footer-brand{position:absolute;left:430px;top:40px;width:340px;height:170px;border-left:1px solid #555;border-right:1px solid #555;text-align:center}
.footer-brand .brand-row{display:flex;align-items:center;justify-content:center;gap:10px;margin-top:28px}
.footer-brand .brand-name{color:#fff;font-size:32px}
.footer-brand .tagline{font-size:10px;color:#aaa;letter-spacing:1px;text-transform:uppercase;margin-top:4px}
.footer-brand .copy{font-size:13px;color:#ccc;margin-top:24px;line-height:1.4}
.footer-contact{position:absolute;left:870px;top:42px}
.footer-contact address{font-style:normal;font-size:13px;line-height:1.55;padding-left:18px}
.footer-contact .phone{margin-top:8px}
</style>
</head>
<body>
<div class="page">

<header class="site-header">
  <div class="brand"><span class="brand-dot"></span><span class="brand-name">lotvantage</span></div>
  <nav class="main-nav">
    <a class="nav-home" href="#">
      <svg width="30" height="26" viewBox="0 0 30 26"><path d="M15 2 2 13h4v11h7v-7h4v7h7V13h4z" fill="#fff"/></svg>
    </a>
    <a class="nav-item" href="#"><b>ADVERTISE</b>with us</a>
    <a class="nav-item" href="#"><b>LISTINGS</b>alert</a>
    <a class="nav-item" href="#"><b>LOT</b>mavens</a>
  </nav>
  <div class="account">
    <a class="register" href="#">New advertiser Register</a>
    <a class="login" href="#">Advertiser login</a>
  </div>
</header>

<section class="hero">
  <div class="photo" role="img" aria-label="Interior of a multi-level shopping mall atrium under a glass dome, with a shopper in the foreground" style="position:absolute;inset:0"></div>
  <h1 class="hero-title">A wide variety of storage spaces!</h1>
  <p class="hero-sub">Looking for stylish modern spaces for your retail business?<br>We have the ideal solution</p>
</section>

<div class="search-band"></div>
<form class="search-panel">
  <div class="search-title">FIND <span>a location</span></div>
  <div class="search-grid">
    <div class="field"><label>Select Category</label><div class="select">Shopping Complexes</div></div>
    <div class="field"><label>Select State/County</label><div class="select">Bangalore</div></div>
    <div class="field"><label>Select Locality/Micro Market</label><div class="select">Select</div></div>
    <div class="field"><label>Transaction Type</label><div class="select">Rent</div></div>
    <div class="field"><label>Enter Keywords</label><div class="select text">Project name, Developers</div></div>
    <div class="field"><div class="search-btn">SEARCH</div></div>
  </div>
</form>

<section class="welcome">
  <div class="welcome-text">
    <h2>WELCOME TO <span>lotvantage !</span></h2>
    <p>lotvantage.com - About Us lotvantage.com is a Specialised Web based platform for Retail Space, featuring properties across India under various formats such as Retail Malls, Shopping Complexes, High-street Shops. lotvantage.com is useful to various category of users as follows</p>
    <div class="audience">
      <div>
        <h3>DEVELOPERS</h3>
        <ul><li>Retailers</li><li>Investors</li><li>Brokers</li></ul>
      </div>
      <p class="audience-note">For advertising their retail developments on a focussed platform that gets accessed by Retailers, Investors and the Broking community</p>
    </div>
  </div>
  <a class="read-more" href="#"><span>Read more</span><i></i></a>

  <div class="category-card">
    <p>Our listings are focused purely on retail spaces and serve retailers, developers, investors and brokers. lotvantage.com is an initiative by a team of engineers, architects and marketing professionals with varied experience in the Real Estate and IT services industries.</p>
    <div class="carousel-arrows"><span></span><span></span></div>
    <div class="category-tiles">
      <div class="tile">
        <div class="photo" role="img" aria-label="Bright retail mall concourse with shopfronts" style="background:linear-gradient(#d7b98c,#8a6c4b)"></div>
        <div class="tile-label">RETAIL MALLS<small>CENTRALLY AIR-CONDITIONED</small></div>
      </div>
      <div class="tile">
        <div class="photo" role="img" aria-label="Shoppers inside a shopping complex" style="background:linear-gradient(#c9d0d6,#6b6e72)"></div>
        <div class="tile-label">SHOPPING COMPLEXES</div>
      </div>
    </div>
  </div>
</section>

<section class="featured">
  <h2 class="section-title">FEATURED PROJECTS</h2>
  <div class="title-rule"></div>
  <div class="filter-tabs"><span class="active">ALL</span><span>MALLS</span><span>COMPLEXES</span><span>STREET SHOPS</span><span>WAREHOUSES</span></div>

  <div class="card-grid row-1">
    <article class="card">
      <div class="photo" role="img" aria-label="Modern shopping complex building facade" style="background:linear-gradient(#cfd8df,#8c8f86)"><div class="tag">SALE /<br>RENT</div></div>
      <div class="card-type">SHOPPING COMPLEX</div>
      <div class="card-body"><h4>CORVIN ALTAN</h4><p>Kestrel Developers presents sustainable modern retail cum office complexes, developed to fulfil the requirements of modern and dynamic businesses.</p></div>
      <div class="card-meta"><div><svg width="9" height="12" viewBox="0 0 9 12"><path d="M4.5 0A4.5 4.5 0 0 0 0 4.5C0 8 4.5 12 4.5 12S9 8 9 4.5A4.5 4.5 0 0 0 4.5 0z" fill="#fff"/></svg>GUJARAT / SURAT</div><div><svg width="11" height="11" viewBox="0 0 11 11"><rect x=".5" y=".5" width="10" height="10" fill="none" stroke="#fff"/></svg>2500 SQ.FT. TO 8588 SQ.FT.</div></div>
    </article>
    <article class="card highlight">
      <div class="photo" role="img" aria-label="High street retail building with glass frontage" style="background:linear-gradient(#b9c6d2,#6f7b84)"><div class="tag">SALE /<br>RENT</div></div>
      <div class="card-type">SHOPPING COMPLEX</div>
      <div class="card-body"><h4>ORVEL 81 HIGH STREET</h4><p>100 meters away from Faridabad's most affluent residential sectors 14 -17. * At the absolute Entrance of Greater Faridabad in Sector 81.</p></div>
      <div class="card-meta"><div><svg width="9" height="12" viewBox="0 0 9 12"><path d="M4.5 0A4.5 4.5 0 0 0 0 4.5C0 8 4.5 12 4.5 12S9 8 9 4.5A4.5 4.5 0 0 0 4.5 0z" fill="#fff"/></svg>HARYANA / FARIDABAD</div><div><svg width="11" height="11" viewBox="0 0 11 11"><rect x=".5" y=".5" width="10" height="10" fill="none" stroke="#fff"/></svg>2500 SQ.FT. TO 8588 SQ.FT.</div></div>
    </article>
    <article class="card">
      <div class="photo" role="img" aria-label="Contemporary mall building exterior" style="background:linear-gradient(#e3e6e8,#9a9b98)"><div class="tag">SALE /<br>RENT</div></div>
      <div class="card-type">SHOPPING COMPLEX</div>
      <div class="card-body"><h4>VERANTA COSMOPOLIS</h4><p>Veranta Cosmopolis is a new age and a trend-setting mix format development. It is surrounded by already populated and upmarket areas like sectors.</p></div>
      <div class="card-meta"><div><svg width="9" height="12" viewBox="0 0 9 12"><path d="M4.5 0A4.5 4.5 0 0 0 0 4.5C0 8 4.5 12 4.5 12S9 8 9 4.5A4.5 4.5 0 0 0 4.5 0z" fill="#fff"/></svg>HARYANA / GURGAON</div><div><svg width="11" height="11" viewBox="0 0 11 11"><rect x=".5" y=".5" width="10" height="10" fill="none" stroke="#fff"/></svg>2500 SQ.FT. TO 8588 SQ.FT.</div></div>
    </article>
    <article class="card">
      <div class="photo" role="img" aria-label="Curved retail complex under blue sky" style="background:linear-gradient(#8fb6d8,#a58a70)"><div class="tag">SALE /<br>RENT</div></div>
      <div class="card-type">SHOPPING COMPLEX</div>
      <div class="card-body"><h4>THE AZURITE</h4><p>Operational Complex with good quality retailers and assured footfalls on Main Sohna Road.</p></div>
      <div class="card-meta"><div><svg width="9" height="12" viewBox="0 0 9 12"><path d="M4.5 0A4.5 4.5 0 0 0 0 4.5C0 8 4.5 12 4.5 12S9 8 9 4.5A4.5 4.5 0 0 0 4.5 0z" fill="#fff"/></svg>HARYANA / GURGAON</div><div><svg width="11" height="11" viewBox="0 0 11 11"><rect x=".5" y=".5" width="10" height="10" fill="none" stroke="#fff"/></svg>2500 SQ.FT. TO 8588 SQ.FT.</div></div>
    </article>
  </div>

  <div class="card-grid row-2">
    <article class="card">
      <div class="photo" role="img" aria-label="Modern shopping complex building facade" style="background:linear-gradient(#cfd8df,#8c8f86)"><div class="tag">SALE /<br>RENT</div></div>
      <div class="card-type">SHOPPING COMPLEX</div>
      <div class="card-body"><h4>CORVIN ALTAN</h4><p>Kestrel Developers presents sustainable modern retail cum office complexes, developed to fulfil the requirements of modern and dynamic businesses.</p></div>
      <div class="card-meta"><div><svg width="9" height="12" viewBox="0 0 9 12"><path d="M4.5 0A4.5 4.5 0 0 0 0 4.5C0 8 4.5 12 4.5 12S9 8 9 4.5A4.5 4.5 0 0 0 4.5 0z" fill="#fff"/></svg>GUJARAT / SURAT</div><div><svg width="11" height="11" viewBox="0 0 11 11"><rect x=".5" y=".5" width="10" height="10" fill="none" stroke="#fff"/></svg>2500 SQ.FT. TO 8588 SQ.FT.</div></div>
    </article>
    <article class="card">
      <div class="photo" role="img" aria-label="High street retail building with glass frontage" style="background:linear-gradient(#b9c6d2,#6f7b84)"><div class="tag">SALE /<br>RENT</div></div>
      <div class="card-type">SHOPPING COMPLEX</div>
      <div class="card-body"><h4>ORVEL 81 HIGH STREET</h4><p>100 meters away from Faridabad's most affluent residential sectors 14 -17. * At the absolute Entrance of Greater Faridabad in Sector 81.</p></div>
      <div class="card-meta"><div><svg width="9" height="12" viewBox="0 0 9 12"><path d="M4.5 0A4.5 4.5 0 0 0 0 4.5C0 8 4.5 12 4.5 12S9 8 9 4.5A4.5 4.5 0 0 0 4.5 0z" fill="#fff"/></svg>HARYANA / FARIDABAD</div><div><svg width="11" height="11" viewBox="0 0 11 11"><rect x=".5" y=".5" width="10" height="10" fill="none" stroke="#fff"/></svg>2500 SQ.FT. TO 8588 SQ.FT.</div></div>
    </article>
    <article class="card">
      <div class="photo" role="img" aria-label="Contemporary mall building exterior" style="background:linear-gradient(#e3e6e8,#9a9b98)"><div class="tag">SALE /<br>RENT</div></div>
      <div class="card-type">SHOPPING COMPLEX</div>
      <div class="card-body"><h4>VERANTA COSMOPOLIS</h4><p>Veranta Cosmopolis is a new age and a trend-setting mix format development. It is surrounded by already populated and upmarket areas like sectors.</p></div>
      <div class="card-meta"><div><svg width="9" height="12" viewBox="0 0 9 12"><path d="M4.5 0A4.5 4.5 0 0 0 0 4.5C0 8 4.5 12 4.5 12S9 8 9 4.5A4.5 4.5 0 0 0 4.5 0z" fill="#fff"/></svg>HARYANA / GURGAON</div><div><svg width="11" height="11" viewBox="0 0 11 11"><rect x=".5" y=".5" width="10" height="10" fill="none" stroke="#fff"/></svg>2500 SQ.FT. TO 8588 SQ.FT.</div></div>
    </article>
    <article class="card">
      <div class="photo" role="img" aria-label="Curved retail complex under blue sky" style="background:linear-gradient(#8fb6d8,#a58a70)"><div class="tag">SALE /<br>RENT</div></div>
      <div class="card-type">SHOPPING COMPLEX</div>
      <div class="card-body"><h4>THE AZURITE</h4><p>Operational Complex with good quality retailers and assured footfalls on Main Sohna Road.</p></div>
      <div class="card-meta"><div><svg width="9" height="12" viewBox="0 0 9 12"><path d="M4.5 0A4.5 4.5 0 0 0 0 4.5C0 8 4.5 12 4.5 12S9 8 9 4.5A4.5 4.5 0 0 0 4.5 0z" fill="#fff"/></svg>HARYANA / GURGAON</div><div><svg width="11" height="11" viewBox="0 0 11 11"><rect x=".5" y=".5" width="10" height="10" fill="none" stroke="#fff"/></svg>2500 SQ.FT. TO 8588 SQ.FT.</div></div>
    </article>
  </div>

  <div class="pagination"><span class="label">Pages 01 of 08</span><span class="box">&lsaquo;</span><span class="box">02</span><span class="box">03</span><span class="box">04</span><span class="box">&rsaquo;</span></div>
</section>

<section class="launch">
  <div class="photo" role="img" aria-label="Blurred interior of a shopping mall with palms and shopfronts" style="position:absolute;inset:0"></div>
  <h2 class="section-title">NEW LAUNCHE PROJECTS</h2>
  <svg class="arrow left" viewBox="0 0 30 50"><path d="M22 8 8 25l14 17" fill="none" stroke="#fff" stroke-width="5"/></svg>
  <svg class="arrow right" viewBox="0 0 30 50"><path d="m8 8 14 17L8 42" fill="none" stroke="#fff" stroke-width="5"/></svg>
  <div class="launch-card">
    <div class="photo" role="img" aria-label="Brightly lit shopping mall entrance at dusk" style="background:linear-gradient(#b7a58c,#5b4a3a)"></div>
    <div class="launch-tag">SALE / RENT</div>
    <div class="launch-bar"><span>CREST ONE</span><i></i><span>RETAIL MALLS</span></div>
  </div>
  <div class="launch-meta">
    <span>UTTAR PRADESH</span><i></i><span>745 SQ FT</span><i></i>
    <svg width="22" height="22" viewBox="0 0 22 22"><circle cx="9" cy="9" r="6" fill="none" stroke="#fff" stroke-width="2.5"/><path d="m13 13 6 6" stroke="#fff" stroke-width="2.5"/></svg>
    <svg width="22" height="22" viewBox="0 0 22 22"><path d="M11 1 21 11 11 21 1 11z" fill="#fff"/><path d="M8 11h6m-2-3 3 3-3 3" stroke="#333" stroke-width="1.6" fill="none"/></svg>
  </div>
</section>

<section class="get-in-touch">
  <h3>Get in touch</h3>
  <div class="socials"><span></span><span></span><span></span><span></span></div>
  <p>Subscribe to our newsletter to stay updated with what is new</p>
  <div class="newsletter-input">Email Address</div>
  <div class="subscribe">Subscribe</div>
</section>

<footer class="site-footer">
  <div class="footer-nav">
    <div class="footer-col">
      <h5>NAVIGATION</h5>
      <ul><li>About Us</li><li>Privacy Policy</li><li>Terms of Use</li><li>Contact Us</li><li>Site Map</li></ul>
    </div>
    <ul class="two"><li>Retail Malls</li><li>Shopping Complex</li><li>High Street Shops</li><li>Retail Warehouses</li></ul>
  </div>
  <div class="footer-brand">
    <div class="brand-row"><span class="brand-dot"></span><span class="brand-name">lotvantage</span></div>
    <div class="tagline">India's leading portal for retail space</div>
    <div class="copy">Copyright © 2013 Northline Retail Hub.com.<br>All rights reserved.</div>
  </div>
  <div class="footer-contact">
    <h5>CONTACT</h5>
    <address>Retail Hub<br>Suite 12, 2nd Level,<br>Lorem Ipsum is simply,<br>Block y, Eastfield - 560417</address>
    <address class="phone">Phone : 000-000-0000</address>
  </div>
</footer>

</div>
</body>
</html>
```